Building certification business in Sydney Australia

Brookvale Assessors is a small business that is currently growing and needs a profession looking website to attract customers and give them all the information they need. The main services we offer currently are pre-purchase building inspections for purchasers and other areas of construction consultancy including pool fencing certificates. Please see attached logos to incorporate to also match colour schemes with. Thanks!

Target Market(s)

Prospective buyers and home owners

Industry/Entity Type

Small Business

Requirements
Must have
• Promote the main services from the home page. Being able to select the type of service/certificate required from the main page and be directed to a specific page that deals with only that service containing the relevant information for that item.
Nice to have
• Small emphasis on the location of our office and areas we service etc.

```html
<!DOCTYPE html>
<html lang="en">
<head>
<meta charset="utf-8">
<title>Brookvale Assessors – Building Certification</title>
<link href="https://fonts.googleapis.com/css2?family=Noto+Serif:wght@400;700&family=Ubuntu:wght@400;500&display=swap" rel="stylesheet">
<style>
:root{
  --teal-dark:#0d7d9e;
  --sky:#1cb0e2;
  --ink:#2b2b2b;
  --muted:#6b6b6b;
  --rule:#e3e3e3;
  --panel:#3a4146;
  --panel-edge:#2c3236;
  --field:#ffffff;
  --orange:#ea6a2c;
  --logo:#2f6f94;
}
*{margin:0;padding:0;box-sizing:border-box}
html,body{width:748px;height:1200px;overflow:hidden;background:#fff}
body{position:relative;font-family:"Noto Serif",serif;color:var(--ink)}
.abs{position:absolute}
.top-band{left:26px;top:0;width:693px;height:24px;background:var(--teal-dark)}
.brand{left:66px;top:42px;display:flex;align-items:center;gap:10px}
.brand-dot{width:14px;height:14px;border-radius:50%;background:var(--logo)}
.brand-name{font-family:"Ubuntu",sans-serif;font-weight:500;font-size:24px;line-height:26px;color:var(--logo);width:150px}
.quote{right:62px;top:56px;text-align:right;font-family:"Ubuntu",sans-serif;font-size:16px;line-height:19px;color:#222}
.nav-top{left:26px;top:118px;width:693px;height:8px;background:var(--teal-dark)}
.nav{left:26px;top:126px;width:693px;height:28px;background:var(--sky)}
.nav-item{position:absolute;top:0;height:28px;line-height:30px;font-size:9px;letter-spacing:.8px;color:#fff;padding:0 11px;border-right:1px solid rgba(255,255,255,.25)}
.nav-item.active{background:#fff;color:var(--sky);top:-1px;height:29px}
.hero-title{left:0;width:748px;top:175px;text-align:center;font-size:16px;font-weight:400}
.hero-sub{left:0;width:748px;top:207px;text-align:center;font-size:11.5px;color:var(--muted)}
.rule{height:1px;background:var(--rule)}
.slide-frame{left:58px;top:253px;width:401px;height:202px;border:1px solid #ddd;padding:3px}
.slide{width:100%;height:100%;background:linear-gradient(180deg,#5c84b0 0%,#a9bfd6 40%,#7a7370 62%,#bdb4a8 100%)}
.section-title{font-size:13px;font-weight:400}
.svc-title{font-size:10px;color:#444;font-weight:400;white-space:nowrap}
.svc-img{width:123px;height:113px}
.svc-text{width:123px;font-size:8px;line-height:14px;color:#555}
.btn{width:56px;height:17px;border-radius:9px;background:var(--sky);color:#fff;font-size:7.5px;font-weight:700;text-align:center;line-height:17px;box-shadow:0 1px 2px rgba(0,0,0,.3)}
.avatar{left:60px;top:833px;width:78px;height:78px;border-radius:50%;border:3px solid var(--sky);background:radial-gradient(circle,#8a6b55,#3d302a)}
.testimonial{left:150px;top:830px;width:311px;font-size:8px;line-height:14.5px;color:#444;text-align:justify}
.author{right:288px;top:912px;font-size:8px;color:var(--teal-dark)}
.booking{left:486px;top:253px;width:199px;height:605px;background:var(--panel);border:1px solid var(--panel-edge);border-radius:4px}
.handle{left:66px;top:14px;width:66px;height:8px;border-radius:5px;background:#1f2427;border:1px solid #5a6268}
.panel-head{left:0;width:199px;text-align:center;font-family:"Ubuntu",sans-serif;font-size:11px;color:#eaeaea}
.field{left:17px;width:162px;height:22px;background:var(--field);border-radius:2px;font-family:"Ubuntu",sans-serif;font-size:7px;color:#aaa;padding:7px 8px 0;box-shadow:inset 0 1px 2px rgba(0,0,0,.3)}
.field.select::after{content:"";position:absolute;right:8px;top:9px;border:3px solid transparent;border-top-color:#555}
.captcha-img{left:17px;top:435px;width:162px;height:32px;background:linear-gradient(90deg,#5a4a40,#9a9a95 50%,#dcdcdc)}
.captcha-link{left:17px;top:534px;font-family:"Ubuntu",sans-serif;font-size:7.5px;color:#ddd}
.book-btn{left:17px;top:555px;width:162px;height:29px;background:var(--orange);border-radius:2px;color:#fff;font-family:"Ubuntu",sans-serif;font-size:10px;text-align:center;line-height:29px}
.pay{top:594px;height:7px;border-radius:1px;background:#c9ccd0}
.info{left:486px;top:876px;width:199px;height:110px;border:1px solid var(--rule);border-radius:3px;font-size:8.5px}
.info-row{position:absolute;left:0;width:199px;height:55px}
.info-label{position:absolute;left:28px;font-weight:700}
.info-value{position:absolute;left:80px;line-height:14px;color:#444}
.map{left:486px;top:1000px;width:199px;height:117px;border:2px solid #fff;box-shadow:0 2px 4px rgba(0,0,0,.25);background:linear-gradient(135deg,#c9d8a8 0%,#e8dcb0 45%,#a8c8e8 75%,#8ab8e0 100%)}
.foot-band{left:26px;top:1133px;width:693px;height:27px;background:var(--sky)}
.foot{left:26px;top:1160px;width:693px;height:26px;background:var(--teal-dark)}
.foot-text{left:32px;top:8px;font-size:7.5px;color:#d6eef6}
.social{top:6px;width:14px;height:14px;border-radius:50%}
</style>
</head>
<body>
<div class="abs top-band"></div>

<header>
  <div class="abs brand"><span class="brand-dot"></span><span class="brand-name">Brookvale Assessors</span></div>
  <div class="abs quote">For an obligation free quote<br>Contact Us +61 2 5550 1234</div>
</header>

<div class="abs nav-top"></div>
<nav class="abs nav">
  <span class="nav-item active" style="left:32px;padding:0 19px">HOME</span>
  <span class="nav-item" style="left:97px">ABOUT</span>
  <span class="nav-item" style="left:153px">SERVICES</span>
  <span class="nav-item" style="left:223px;border:none">CONTACT</span>
</nav>

<h1 class="abs hero-title">Trusted and Reliable Building Certification</h1>
<p class="abs hero-sub">With a commitment to client satisfaction and quality certification, why not book us now?</p>
<div class="abs rule" style="left:58px;top:237px;width:628px"></div>

<div class="abs slide-frame"><div class="slide" role="img" aria-label="Modern single-storey home with skillion roof and gravel driveway"></div></div>

<h2 class="abs section-title" style="left:58px;top:467px">Our Services</h2>
<svg class="abs" style="left:402px;top:468px" width="56" height="16" viewBox="0 0 56 16">
  <circle cx="8" cy="8" r="7.5" fill="#1cb0e2"/><path d="M9.5 4.5 6 8l3.5 3.5" stroke="#fff" stroke-width="2" fill="none"/>
  <circle cx="28" cy="8" r="7.5" fill="#1cb0e2"/><rect x="25" y="4.5" width="2" height="7" fill="#fff"/><rect x="29" y="4.5" width="2" height="7" fill="#fff"/>
  <circle cx="48" cy="8" r="7.5" fill="#1cb0e2"/><path d="M46.5 4.5 50 8l-3.5 3.5" stroke="#fff" stroke-width="2" fill="none"/>
</svg>
<div class="abs rule" style="left:58px;top:495px;width:402px"></div>

<section>
  <h3 class="abs svc-title" style="left:58px;top:509px">Pre-Purchase Inspection</h3>
  <div class="abs svc-img" style="left:58px;top:530px;background:linear-gradient(180deg,#1d2a3e,#5a4a3a 55%,#2f6b5a)" role="img" aria-label="House at dusk with lit windows and pool"></div>
  <p class="abs svc-text" style="left:58px;top:652px">Pre-Purchase Building inspections are essential because they ensure..enter text here to introduce the service</p>
  <div class="abs btn" style="left:58px;top:722px">Read More</div>

  <h3 class="abs svc-title" style="left:197px;top:509px">Pool Certification</h3>
  <div class="abs svc-img" style="left:197px;top:530px;background:linear-gradient(180deg,#4e7a3e,#8a9a8a 40%,#2a6eb0 70%,#c8c4bc)" role="img" aria-label="Backyard swimming pool with landscaped garden"></div>
  <p class="abs svc-text" style="left:197px;top:652px">Our pool inspection service provides for peace of mind..enter text here to introduce the service</p>
  <div class="abs btn" style="left:197px;top:722px">Read More</div>

  <h3 class="abs svc-title" style="left:336px;top:509px">Building Consultancy</h3>
  <div class="abs svc-img" style="left:336px;top:530px;background:linear-gradient(135deg,#3f78b8,#7fa6c8 45%,#c7c2b6 75%,#b88a5a)" role="img" aria-label="Construction worker holding a hard hat beside scaffolding"></div>
  <p class="abs svc-text" style="left:336px;top:652px">Our building and construction consultancy service provides for....enter text here to introduce the service to the reader.</p>
  <div class="abs btn" style="left:336px;top:736px">Read More</div>
</section>

<h2 class="abs section-title" style="left:58px;top:781px">What our customers say:</h2>
<div class="abs rule" style="left:58px;top:813px;width:402px"></div>
<div class="abs avatar" role="img" aria-label="Customer photo"></div>
<p class="abs testimonial">I have engaged Brookvale Assessors on multiple occasions to assist in the certification of construction works and for pre-purchase building inspections for prospective buyers of our properties. I have found their service to be affordable and importantly the team at Brookvale Assessors are reliable and always turn up on time. I would happily recommend Brookvale Assessors.</p>
<p class="abs author">Daniel @ Harbour Print Co</p>

<aside class="abs booking">
  <div class="abs handle"></div>
  <div class="abs panel-head" style="top:36px">Book an Appointment Online</div>
  <div class="abs field" style="top:65px">Name</div>
  <div class="abs field" style="top:98px">Email</div>
  <div class="abs field" style="top:130px">Contact Number</div>
  <div class="abs panel-head" style="top:161px">Select Date and Time</div>
  <div class="abs field select" style="top:188px;width:159px">Select Service</div>
  <div class="abs field" style="top:226px">Select Date</div>
  <div class="abs field select" style="top:257px;width:159px">Select Time</div>
  <div class="abs field" style="top:294px">Service Price</div>
  <div class="abs panel-head" style="top:325px">Enter a message</div>
  <div class="abs field" style="top:353px;height:66px">Your Message (Optional)</div>
  <div class="abs captcha-img" role="img" aria-label="Verification image"></div>
  <div class="abs panel-head" style="top:476px">Enter the words below</div>
  <div class="abs field" style="top:501px"></div>
  <div class="abs captcha-link">Get another CAPTCHA</div>
  <div class="abs book-btn">Book Appointment</div>
  <div class="abs pay" style="left:50px;width:32px"></div>
  <div class="abs pay" style="left:86px;width:10px"></div>
  <div class="abs pay" style="left:99px;width:10px"></div>
  <div class="abs pay" style="left:112px;width:10px"></div>
  <div class="abs pay" style="left:125px;width:10px"></div>
</aside>

<div class="abs info">
  <div class="info-row" style="top:0;border-bottom:1px solid var(--rule)">
    <svg class="abs" style="left:10px;top:17px" width="11" height="11" viewBox="0 0 11 11"><circle cx="5.5" cy="5.5" r="4.5" fill="none" stroke="#1a9cc8" stroke-width="1.5"/><path d="M5.5 3v2.7l1.8 1" stroke="#1a9cc8" stroke-width="1.2" fill="none"/></svg>
    <span class="info-label" style="top:16px">Hours</span>
    <span class="info-value" style="top:16px">Mon-Fri: 7:00am - 4:00pm<br>Sat-Sun: Closed</span>
  </div>
  <div class="info-row" style="top:55px">
    <svg class="abs" style="left:11px;top:21px" width="9" height="13" viewBox="0 0 9 13"><path d="M4.5 12.5S.5 7.5.5 4.5a4 4 0 0 1 8 0c0 3-4 8-4 8z" fill="#1a9cc8"/><circle cx="4.5" cy="4.5" r="1.5" fill="#fff"/></svg>
    <span class="info-label" style="top:21px">Address</span>
    <span class="info-value" style="top:21px">Sydney, NSW Australia</span>
  </div>
</div>
<svg class="abs" style="left:579px;top:985px" width="14" height="8" viewBox="0 0 14 8"><path d="M0 0h14L7 7z" fill="#fff" stroke="#e3e3e3"/><rect x="0" y="0" width="14" height="1" fill="#fff"/></svg>
<div class="abs map" role="img" aria-label="Map of the Sydney service area"></div>

<footer>
  <div class="abs foot-band"></div>
  <div class="abs foot">
    <span class="abs foot-text">Brookvale Assessors. All Rights Reserved 2014</span>
    <span class="abs social" style="left:561px;background:#1bb5a0"></span>
    <span class="abs social" style="left:582px;background:#3b5c9c"></span>
    <span class="abs social" style="left:603px;background:#e07b2a"></span>
    <span class="abs social" style="left:624px;background:#222"></span>
    <span class="abs social" style="left:645px;background:#c0392b"></span>
  </div>
</footer>
</body>
</html>
```